TQ Regulatory Partners - Biz Card - Re-do

I would like a re-do on my business card.

See my Internet site - tqregpartners.com

1) Remove direct phone line.
2) Add company moto - integrity, diligence, and excellence
3) Add Consulting Services listing:
-Benefit Technology
-ERISA Compliance
-Contract/Vendor Management
-Human Resource/Payroll
-Medical/Prescription Drug
-Integrated Leave of Absence

Target Market(s)

Employee benefit consulting and insurance purchasers, Usually human resource executives

Industry/Entity Type

Human Resource

Contact Information for Business Card

Same business card color scheme, logo,

Font styles to use
Sans Serif

Requirements
Must have
• Same color scheme and logo. Remove direct phone number. Keep all numbers, internet address.

```html
<!DOCTYPE html>
<html lang="en">
<head>
<meta charset="utf-8">
<title>TQ Regulatory Partners – Business Card</title>
<link href="https://fonts.googleapis.com/css2?family=Lato:wght@400;700&display=swap" rel="stylesheet">
<style>
  :root {
    --plum: #6b1a48;
    --plum-dark: #521437;
    --paper: #ffffff;
    --paper-shade: #f1f1f1;
    --ink: #555555;
    --backdrop: #d9d9dc;
  }
  * { box-sizing: border-box; margin: 0; padding: 0; }
  html, body { width: 1200px; height: 900px; overflow: hidden; }
  body {
    background: var(--backdrop);
    font-family: "Lato", Arial, sans-serif;
    display: flex; flex-direction: column; align-items: center; justify-content: center; gap: 60px;
  }
  .card {
    position: relative; width: 560px; height: 320px;
    box-shadow: 0 10px 28px rgba(0,0,0,.25);
    overflow: hidden;
  }
  /* Front */
  .card-front { background: linear-gradient(135deg, var(--paper) 40%, var(--paper-shade)); color: var(--ink); }
  .brand { position: absolute; left: 30px; top: 26px; display: flex; align-items: center; gap: 14px; }
  .brand-dot { width: 64px; height: 64px; border-radius: 50%; background: var(--plum); }
  .brand-name { font-size: 25px; line-height: 1.05; color: var(--ink); font-weight: 400; }
  .motto {
    position: absolute; left: 30px; top: 132px;
    font-size: 11.5px; font-weight: 700; letter-spacing: .6px; color: var(--plum);
  }
  .person { position: absolute; right: 52px; top: 124px; text-align: right; }
  .person-name { font-size: 20px; font-weight: 700; color: var(--plum); letter-spacing: .5px; }
  .person-title { font-size: 12px; color: var(--ink); margin-top: 2px; }
  .rule { position: absolute; left: 30px; right: 52px; top: 174px; height: 1.5px; background: var(--plum); }
  .edge-tab { position: absolute; right: 0; top: 150px; width: 22px; height: 30px; background: var(--plum); }
  .contacts { position: absolute; left: 30px; top: 192px; list-style: none; font-size: 12.5px; line-height: 1.65; }
  .contacts li { display: flex; align-items: center; gap: 8px; }
  .contacts svg { width: 10px; height: 10px; fill: var(--plum); }
  .address { position: absolute; right: 52px; bottom: 32px; text-align: right; font-size: 12.5px; line-height: 1.6; }
  /* Back */
  .card-back {
    background: linear-gradient(160deg, var(--plum) 0%, var(--plum-dark) 100%);
    color: #ece6ea; text-align: center;
  }
  .back-dot { width: 70px; height: 70px; border-radius: 50%; background: #e8e4e6; margin: 40px auto 16px; }
  .back-name { font-size: 32px; font-weight: 400; color: #ece6ea; }
  .services { list-style: none; margin-top: 20px; font-size: 13px; line-height: 1.7; letter-spacing: .3px; }
</style>
</head>
<body>
  <section class="card card-front">
    <div class="brand">
      <span class="brand-dot"></span>
      <span class="brand-name">TQ Regulatory<br>Partners</span>
    </div>
    <p class="motto">INTEGRITY, DILIGENCE, AND EXCELLENCE</p>
    <div class="person">
      <p class="person-name">DANIEL MARSH</p>
      <p class="person-title">President</p>
    </div>
    <div class="rule"></div>
    <div class="edge-tab"></div>
    <ul class="contacts">
      <li><svg viewBox="0 0 10 10"><path d="M2 0h2l1 3-1.5 1a6 6 0 0 0 2.5 2.5L7 5l3 1v2a2 2 0 0 1-2 2A8 8 0 0 1 0 2a2 2 0 0 1 2-2z"/></svg>555.210.4381</li>
      <li><svg viewBox="0 0 10 10"><rect x="0" y="1" width="10" height="8" rx="1"/></svg>555.210.4382</li>
      <li><svg viewBox="0 0 10 10"><path d="M0 2h10v6H0z M0 2l5 3.5L10 2" stroke="#fff" stroke-width=".8"/></svg>dmarsh@tqregpartners.com</li>
      <li><svg viewBox="0 0 10 10"><circle cx="5" cy="5" r="5"/></svg>www.tqregpartners.com</li>
    </ul>
    <p class="address">418 Harbor Street NE, Suite 300<br>Lakeview, MI 49012</p>
  </section>

  <section class="card card-back">
    <div class="back-dot"></div>
    <p class="back-name">TQ Regulatory Partners</p>
    <ul class="services">
      <li>Benefit Technology | ERISA Compliance</li>
      <li>Contract/Vendor Management | Human Resource/Payroll</li>
      <li>Medical/Prescription Drug | Integrated Leave of Absence</li>
    </ul>
  </section>
</body>
</html>
```